we need a business card. We are an online company that provides work life balance services to our members. our website can be viewed at www.qorvenly.com.au
Our company logo is attached as well as a business card look that i like.

```html
<!DOCTYPE html>
<html lang="en">
<head>
<meta charset="utf-8">
<title>Qorvenly business card</title>
<link rel="stylesheet" href="https://fonts.googleapis.com/css2?family=Arimo:wght@400&family=Open+Sans:wght@400&family=Crimson+Text:ital@1&display=swap">
<style>
  :root {
    --page: #ffffff;
    --green-light: #7dba43;
    --green-mid: #64972f;
    --green-dark: #4a7128;
    --back-light: #6ea823;
    --back-dark: #2f5510;
    --ink-white: #ffffff;
    --name-grey: #d4d6d2;
    --tagline-green: #b9e07e;
    --mark-dot: #9bd159;
  }
  html, body {
    margin: 0;
    padding: 0;
    width: 911px;
    height: 1200px;
    overflow: hidden;
    background: var(--page);
  }
  .sheet {
    position: relative;
    width: 911px;
    height: 1200px;
  }
  .card-front {
    position: absolute;
    left: 243px;
    top: 27px;
    width: 391px;
    height: 667px;
    background: radial-gradient(ellipse 60% 55% at 50% 48%, var(--green-light) 0%, var(--green-mid) 55%, var(--green-dark) 100%);
    color: var(--ink-white);
    font-family: "Arimo", Arial, sans-serif;
    text-align: center;
  }
  .contact-line {
    position: absolute;
    left: 0;
    width: 100%;
    margin: 0;
    font-size: 19px;
    line-height: 1;
    white-space: nowrap;
  }
  .contact-line--phone { top: 89px; }
  .contact-line--email { top: 125px; }
  .contact-line--web { top: 491px; }
  .contact-line--street,
  .contact-line--suburb { font-variant: small-caps; font-size: 19px; }
  .contact-line--street { top: 528px; }
  .contact-line--suburb { top: 565px; }
  .front-name {
    position: absolute;
    left: 0;
    top: 305px;
    width: 100%;
    display: flex;
    justify-content: center;
    align-items: center;
    gap: 10px;
    font-size: 30px;
    line-height: 1;
  }
  .front-name__dot {
    width: 16px;
    height: 16px;
    border-radius: 50%;
    background: var(--mark-dot);
  }
  .card-back {
    position: absolute;
    left: 82px;
    top: 718px;
    width: 706px;
    height: 407px;
    overflow: hidden;
  }
  .card-back__ornament {
    position: absolute;
    inset: 0;
    background: radial-gradient(ellipse 80% 90% at 55% 20%, var(--back-light) 0%, #4f8418 50%, var(--back-dark) 100%);
  }
  .brand-name {
    position: absolute;
    left: 168px;
    top: 174px;
    margin: 0;
    font-family: "Open Sans", Arial, sans-serif;
    font-weight: 400;
    font-size: 60px;
    line-height: 1;
    letter-spacing: -1px;
    color: var(--name-grey);
  }
  .tagline {
    position: absolute;
    left: 344px;
    top: 239px;
    margin: 0;
    font-family: "Crimson Text", Georgia, serif;
    font-style: italic;
    font-size: 19px;
    line-height: 1;
    color: var(--tagline-green);
    white-space: nowrap;
  }
</style>
</head>
<body>
<main class="sheet">
  <section class="card-front" aria-label="Card front with contact details">
    <p class="contact-line contact-line--phone">PH- 02 9400 1357 FAX- 02 9400 1358</p>
    <p class="contact-line contact-line--email">info@qorvenly.com.au</p>
    <div class="front-name"><span class="front-name__dot"></span><span>qorvenly</span></div>
    <p class="contact-line contact-line--web">www.qorvenly.com.au</p>
    <p class="contact-line contact-line--street">First Floor, 48 Harbour View Road</p>
    <p class="contact-line contact-line--suburb">Waverton Point, NSW 2061</p>
  </section>

  <section class="card-back" aria-label="Card back with company name">
    <div class="card-back__ornament" role="img" aria-label="Green background with darker swirling vines and leaves"></div>
    <h1 class="brand-name">qorvenly</h1>
    <p class="tagline">living better, working smarter</p>
  </section>
</main>
</body>
</html>
```